Website for Fernvale Harmony Chapel

Wordpress website design required for Fernvale Harmony Chapel. We are a family oriented church catering for age groups from school age to elderly people. The church has a wide variety of activities which it coordinates. The idea is to describe the activities on the activities page, but cross-link them to show which would be applicable to the different age groups.

We would like an inviting website which is easy to read and navigate.

Target Market(s)

Very wide audience - from school age youth to elderly people, so design and style should cater for both audiences.

Industry/Entity Type

Church

Coding

Coded - Design and coding required

Number of Pages Required

5+ page

Font styles to use
Sans Serif

Colors
0255a3
ffffff
0792cd
f78f20

Requirements
Must have
• Inviting website.
• Clear readable font.
• Space to import photos to balance text on each page.
• Need to project a dynamic and progressive feel for the church.
• Easy to navigate.
Nice to have
• Scrolling photos on pages. Ability to enter questions/ comments/prayer requests on Home page.
Should not have
• Conservative audience, so should not be too bold.

```html
<!DOCTYPE html>
<html lang="en">
<head>
<meta charset="utf-8">
<title>Fernvale Harmony Chapel</title>
<link rel="stylesheet" href="https://fonts.googleapis.com/css2?family=Lato:wght@400;700;900&display=swap">
<style>
:root{
  --blue:#0792cd;
  --navy:#0255a3;
  --orange:#f78f20;
  --dark:#222222;
  --ink:#1d1d1d;
  --muted:#8a8a8a;
  --rule:#d2d2d2;
  --white:#ffffff;
}
*{margin:0;padding:0;box-sizing:border-box}
html,body{width:1200px;height:2848px;overflow:hidden}
body{position:relative;background:var(--white);font-family:'Lato',sans-serif;color:var(--ink)}
.abs{position:absolute}

/* top bar */
.topbar{left:0;top:0;width:1200px;height:42px;background:var(--dark)}
.call{left:104px;top:0;height:42px;display:flex;align-items:center;gap:12px;color:var(--white)}
.call strong{font-size:22px;font-weight:700;letter-spacing:1px}
.call span{font-size:18px;color:#bdbdbd}
.socials{display:flex;gap:12px;align-items:center}
.socials i{display:block;width:20px;height:20px;background:var(--white);border-radius:3px}
.topbar-socials{right:104px;top:11px}

/* header */
.brand{left:100px;top:138px;display:flex;align-items:center;gap:10px}
.brand-dot{width:20px;height:20px;border-radius:50%;background:var(--navy)}
.brand-name{font-size:26px;font-weight:700;color:var(--navy)}
.partner-mark{left:960px;top:58px;width:130px;height:130px;border-radius:50%;background:var(--dark)}

/* nav */
.nav{left:0;top:203px;width:1200px;height:59px;background:var(--blue)}
.nav a{position:absolute;top:19px;font-size:17px;font-weight:700;color:var(--white);text-decoration:none;letter-spacing:.3px;white-space:nowrap}
.nav a.active{color:#fff3e2}
.nav a.active::after{content:"";position:absolute;left:0;right:0;top:28px;height:4px;background:var(--orange);border-radius:2px}

/* hero */
.hero{left:0;top:262px;width:1200px;height:454px;background:linear-gradient(100deg,#3a3a32 0%,#5b6a45 35%,#6f8a4a 60%,#3f5030 100%)}
.hero-copy{left:659px;top:376px;color:var(--white)}
.hero-copy .kicker{font-size:29px;font-weight:700;letter-spacing:6px}
.hero-copy h1{font-size:44px;font-weight:700;letter-spacing:7px;line-height:1.05}
.hero-copy p{font-size:19px;font-weight:700;margin-top:12px}
.btn-more{left:659px;top:522px;width:153px;height:47px;background:var(--white);border-radius:5px;font-size:19px;font-weight:700;color:var(--ink);display:flex;align-items:center;justify-content:center;letter-spacing:.5px}
.arrow{top:446px}
.dots{left:510px;top:678px;display:flex;gap:16px}
.dots i{display:block;width:26px;height:26px;border-radius:50%;background:var(--white)}
.dots i.on{background:var(--blue);border:3px solid var(--white)}

/* section titles */
.title{display:flex;align-items:center;font-size:27px;font-weight:900;letter-spacing:2px;color:var(--ink);white-space:nowrap}
.title b{color:var(--blue);font-weight:900}
.title::after{content:"";flex:1;height:4px;background:var(--rule);margin-left:22px}
.body-text{font-size:17px;font-weight:700;line-height:38px;letter-spacing:1.2px;color:var(--ink)}

/* activities */
.tile{top:1050px;width:240px;height:255px}
.tile-text{left:258px;top:1104px;color:var(--white);font-size:19px;font-weight:700;line-height:30px;letter-spacing:1px}
.tile-text .date{color:var(--blue)}

/* service box */
.service{left:754px;top:1345px;width:344px;height:327px;background:var(--orange);border:1px solid #c46b10;border-radius:4px;padding:20px 22px}
.service h3{font-size:26px;font-weight:400;letter-spacing:1.5px;color:var(--dark);margin-bottom:8px}
.service p{font-size:16px;font-weight:700;line-height:30px;letter-spacing:1.2px;color:var(--dark)}

/* prayer */
.prayer{left:0;top:1709px;width:1200px;height:125px;background:var(--blue)}
.prayer h2{position:absolute;left:100px;top:44px;font-size:32px;font-weight:700;letter-spacing:6px;color:var(--white)}
.prayer-input{left:650px;top:1751px;width:303px;height:47px;background:var(--white);border-radius:5px 0 0 5px;font-size:17px;color:#333;padding:14px 18px}
.prayer-btn{left:953px;top:1751px;width:145px;height:47px;background:var(--dark);border-radius:0 5px 5px 0;color:var(--white);font-size:18px;font-weight:700;letter-spacing:1px;display:flex;align-items:center;justify-content:center}

/* news */
.news{left:100px;width:318px;height:100px;border-bottom:2px solid #eeeeee}
.news-date{position:absolute;left:0;top:0;width:50px;height:70px;background:#ededed;text-align:center;color:#555}
.news-date .d{font-size:22px;display:block;padding-top:6px}
.news-date .m{font-size:10px;display:block}
.news-date .y{position:absolute;left:0;bottom:0;width:50px;height:20px;background:var(--orange);color:var(--white);font-size:11px;font-weight:700;line-height:20px}
.news h4{position:absolute;left:65px;top:0;font-size:14px;font-weight:700;color:#333}
.news p{position:absolute;left:65px;top:22px;width:250px;font-size:12px;line-height:21px;color:#9a9a9a}
.news .meta{position:absolute;left:65px;top:75px;font-size:10px;color:#9a9a9a;display:flex;gap:22px}
.slider-img{left:442px;top:1922px;width:656px;height:328px;background:linear-gradient(180deg,#3d7fc1 0%,#7aa6d4 50%,#dfe7ee 100%)}
.slider-dots{left:1036px;top:2219px;display:flex;gap:7px}
.slider-dots i{display:block;width:9px;height:9px;border-radius:50%;background:#444}

/* form */
.field{height:46px;border:2px solid #9a9a9a;border-radius:6px;background:#fafafa;font-size:16px;color:#666;padding:11px 18px;letter-spacing:.5px}
.submit{left:608px;top:2512px;width:488px;height:46px;background:var(--orange);border-radius:5px;color:var(--white);font-size:16px;font-weight:700;letter-spacing:1.5px;display:flex;align-items:center;justify-content:center}

/* contacts */
.contact{top:2610px;width:360px;text-align:center}
.contact svg{display:block;margin:0 auto 14px}
.contact h5{font-size:24px;font-weight:400;letter-spacing:1.5px;color:var(--dark)}
.contact p{font-size:16px;line-height:24px;color:#555;margin-top:4px}

/* footer */
.footer{left:0;top:2795px;width:1200px;height:53px;background:var(--dark)}
.footer p{position:absolute;left:100px;top:16px;font-size:17px;color:var(--white);font-weight:700;letter-spacing:.5px}
.footer p b{color:var(--orange)}
.footer .socials{position:absolute;right:104px;top:13px;gap:18px}
.footer .socials i{width:27px;height:27px}
</style>
</head>
<body>

<!-- top bar -->
<div class="abs topbar"></div>
<div class="abs call">
  <svg width="26" height="26" viewBox="0 0 26 26"><circle cx="13" cy="13" r="11.5" fill="none" stroke="#f78f20" stroke-width="2"/><path d="M9 7.5l2.5 0 1 3-1.6 1.2a8 8 0 0 0 3.4 3.4l1.2-1.6 3 1v2.5c0 .6-.6 1-1.2 1A10 10 0 0 1 8 8.7c0-.6.4-1.2 1-1.2z" fill="#f78f20"/></svg>
  <strong>CALL US</strong><span>+1 (0) 555 0142 880</span>
</div>
<div class="abs socials topbar-socials"><i></i><i></i><i></i><i></i><i></i><i></i></div>

<!-- header -->
<div class="abs brand"><span class="brand-dot"></span><span class="brand-name">Fernvale Harmony Chapel</span></div>
<div class="abs partner-mark"></div>

<!-- nav -->
<nav class="abs nav">
  <a class="active" style="left:104px">HOME</a>
  <a style="left:203px">ABOUT US</a>
  <a style="left:346px">ACTIVITIES</a>
  <a style="left:492px">EVENT CALENDER</a>
  <a style="left:697px">AGE GROUP</a>
  <a style="left:849px">CONTACT US</a>
</nav>

<!-- hero -->
<div class="abs hero" role="img" aria-label="Photo of a woman looking up toward sunlit green vines"></div>
<div class="abs hero-copy">
  <div class="kicker">MY MIND IS MY</div>
  <h1>OWN CHURCH</h1>
  <p>Transforming lives that change the world.</p>
</div>
<div class="abs btn-more">READ MORE</div>
<svg class="abs arrow" style="left:10px" width="36" height="36" viewBox="0 0 36 36"><path d="M26 2L8 18l18 16" fill="none" stroke="#fff" stroke-width="6"/></svg>
<svg class="abs arrow" style="left:1154px" width="36" height="36" viewBox="0 0 36 36"><path d="M10 2l18 16-18 16" fill="none" stroke="#fff" stroke-width="6"/></svg>
<div class="abs dots"><i class="on"></i><i></i><i></i><i></i></div>

<!-- mission -->
<div class="abs title" style="left:100px;top:756px;width:996px"><span>OUR <b>MISSION</b></span></div>
<p class="abs body-text" style="left:100px;top:806px;width:996px">Lorem Ipsum is simply dummy text of the printing and typesetting industry.Lorem Ipsum has been the industry's standard dummy text ever since the 1500s, when an unknown printer took a galley of type and scrambled it to make a type specimen book. It has survived not only five centuries, but also the leap into electronic typesetting, remaining essentially unchanged.</p>

<!-- activities -->
<div class="abs title" style="left:100px;top:995px;width:996px"><span>OUR <b>ACTIVITIES</b></span></div>
<div class="abs tile" style="left:0;background:linear-gradient(160deg,#7d7a74,#3f5670)" role="img" aria-label="Photo of two school children in uniform"></div>
<div class="abs tile" style="left:240px;background:linear-gradient(160deg,#555,#3a3a3a)" role="img" aria-label="Dark grey stone texture behind event text"></div>
<div class="abs tile" style="left:480px;background:linear-gradient(180deg,#c9a13a,#5a3e22)" role="img" aria-label="Photo of a speaker addressing a large hall"></div>
<div class="abs tile" style="left:720px;background:linear-gradient(160deg,#d24fb0,#f0a04a 60%,#5a1f6a)" role="img" aria-label="Photo of a worship concert with a lit cross"></div>
<div class="abs tile" style="left:960px;background:linear-gradient(120deg,#0a0a0a,#4a3a30 55%,#111)" role="img" aria-label="Photo of a man praying with folded hands"></div>
<div class="abs tile-text"><span class="date">OCT 29, 2015</span><br>VARRAS LUCTUS<br>MALESUADA TI CRAS<br>LUCTUS MALESUADA<br>TIPORTA..</div>

<!-- minister -->
<div class="abs title" style="left:100px;top:1371px;width:612px"><span>MINISTER'S <b>SAYS</b></span></div>
<p class="abs body-text" style="left:100px;top:1417px;width:620px">Lorem Ipsum is simply dummy text of the printing and typesetting industry.Lorem Ipsum has been the industry's standard dummy text ever since the 1500s, when an unknown printer took a galley of type and scrambled it to make a type specimen book. It has survived not only five centuries, but also the leap into electronic typesetting, remaining essentially unchanged.</p>
<div class="abs service">
  <h3>SERVICE TIMES</h3>
  <p>Sundays at 9:30 and 11:00 Worship Center.8:15am Pastor's Class Church Hall</p>
  <h3 style="margin-top:18px">LOCATION</h3>
  <p>Lorem Ipsum is simply dummy text of the printing and Lorem Ipsum has been the industry's..</p>
</div>

<!-- prayer -->
<div class="abs prayer"><h2>ENTER PRAYER REQUEST</h2></div>
<div class="abs prayer-input">Your Email Adress</div>
<div class="abs prayer-btn">SUBMIT</div>

<!-- news -->
<div class="abs title" style="left:100px;top:1866px;width:318px"><span>LATEST <b>NEWS</b></span></div>
<div class="abs news" style="top:1922px">
  <div class="news-date"><span class="d">24</span><span class="m">AUG</span><span class="y">2014</span></div>
  <h4>Utsit amet risus acur venenat</h4>
  <p>Polint stdunt dolor sit amet constetur adipisicing elit sed do eiusmod</p>
  <div class="meta"><span>John Doe</span><span>4 Comments</span></div>
</div>
<div class="abs news" style="top:2043px">
  <div class="news-date"><span class="d">22</span><span class="m">AUG</span><span class="y">2014</span></div>
  <h4>Massa the quis commodo ligula</h4>
  <p>Polint stdunt dolor sit amet constetur adipisicing elit sed do eiusmod</p>
  <div class="meta"><span>John Doe</span><span>0 Comments</span></div>
</div>
<div class="abs news" style="top:2164px;border-bottom:none">
  <div class="news-date"><span class="d">18</span><span class="m">AUG</span><span class="y">2014</span></div>
  <h4>Quisque aquam sapien malesua</h4>
  <p>Polint stdunt dolor sit amet constetur adipisicing elit sed do eiusmod</p>
  <div class="meta"><span>John Doe</span><span>0 Comments</span></div>
</div>

<div class="abs title" style="left:442px;top:1866px;width:656px"><span>IMAGE <b>SLIDER</b></span></div>
<div class="abs slider-img" role="img" aria-label="Photo of a mother carrying her young son against a blue sky"></div>
<div class="abs slider-dots"><i></i><i></i><i></i></div>

<!-- message form -->
<div class="abs title" style="left:100px;top:2315px;width:996px"><span>SEND A <b>MESSAGE</b></span></div>
<div class="abs field" style="left:100px;top:2379px;width:496px">Your Name</div>
<div class="abs field" style="left:100px;top:2446px;width:496px">Your Email</div>
<div class="abs field" style="left:100px;top:2512px;width:496px">Subject</div>
<div class="abs field" style="left:608px;top:2379px;width:488px;height:111px">Your Message</div>
<div class="abs submit">SUBMIT</div>

<!-- contacts -->
<div class="abs contact" style="left:69px">
  <svg width="50" height="50" viewBox="0 0 50 50"><circle cx="25" cy="25" r="23" fill="none" stroke="#0792cd" stroke-width="3"/><path d="M13 25l12-11 12 11h-3v11h-6v-7h-6v7h-6V25z" fill="#0792cd"/></svg>
  <h5>OUR ADRESS</h5>
  <p>2750 Linden Grove Road,<br>Suite 410</p>
</div>
<div class="abs contact" style="left:422px">
  <svg width="50" height="50" viewBox="0 0 50 50"><circle cx="25" cy="25" r="23" fill="none" stroke="#0792cd" stroke-width="3"/><rect x="13" y="17" width="24" height="16" fill="none" stroke="#0792cd" stroke-width="2.5"/><path d="M13 17l12 9 12-9" fill="none" stroke="#0792cd" stroke-width="2.5"/></svg>
  <h5>OUR EMAIL</h5>
  <p>hello@fernvalechapel.org</p>
</div>
<div class="abs contact" style="left:781px">
  <svg width="50" height="50" viewBox="0 0 50 50"><circle cx="25" cy="25" r="23" fill="none" stroke="#0792cd" stroke-width="3"/><path d="M17 13h5l2 6-3 2.5a15 15 0 0 0 7 7l2.5-3 6 2v5c0 1.2-1 2-2.2 2A21 21 0 0 1 15 15.2c0-1.2.8-2.2 2-2.2z" fill="#0792cd"/></svg>
  <h5>CALL US</h5>
  <p>+1 (0) 555 0142 880</p>
</div>

<!-- footer -->
<div class="abs footer">
  <p><b>© 2016</b> Fernvale Harmony. All Rights Reserved.</p>
  <div class="socials"><i></i><i></i><i></i><i></i><i></i><i></i></div>
</div>

</body>
</html>
```